Brivora Collective Business Card Design

We need a business card design for Brivora Collective. We are a healthcare recruiting, wellness and education company. We partner with medical facilities to find quality candidates. We also offer free wellness courses.
The final design should communicate an emphasis on recruiting and wellness
The main purpose of the business card is to utilized it for networking events, give to hospitals, executives, VCs surgery centers and clinics. I want it to be sleek, clean, use of our brand colors and professional.

```html
<!DOCTYPE html>
<html lang="en">
<head>
<meta charset="utf-8">
<title>Brivora Collective Business Card</title>
<link rel="stylesheet" href="https://fonts.googleapis.com/css2?family=Open+Sans:wght@600;700&display=swap">
<style>
  :root {
    --backdrop: #dddddd;
    --paper: #ffffff;
    --brand: #02564f;
    --tone-light: #9bbcb8;
    --tone-mid: #386660;
    --tone-dark: #0d2724;
  }
  * { margin: 0; padding: 0; box-sizing: border-box; }
  html, body {
    width: 1200px;
    height: 1200px;
    overflow: hidden;
    background: var(--backdrop);
    font-family: "Open Sans", Arial, sans-serif;
  }
  .card {
    position: absolute;
    left: 222px;
    width: 756px;
    height: 432px;
    background: var(--paper);
    overflow: hidden;
  }
  .card--info { top: 138px; }
  .card--brand { top: 630px; }
  .card__accent {
    position: absolute;
  }
  .card--info .card__accent {
    left: 0;
    top: 0;
    width: 200px;
    height: 100%;
    background: linear-gradient(90deg, var(--tone-dark) 0%, var(--tone-mid) 55%, var(--tone-light) 100%);
  }
  .card--brand .card__accent {
    left: 0;
    bottom: 0;
    width: 100%;
    height: 110px;
    background: linear-gradient(180deg, var(--tone-light) 0%, var(--tone-mid) 50%, var(--tone-dark) 100%);
  }
  .brand-name {
    position: absolute;
    color: var(--brand);
    font-weight: 700;
    white-space: nowrap;
    transform: translate(-50%, -50%);
  }
  .card--info .brand-name {
    left: 491px;
    top: 80px;
    font-size: 26px;
    display: flex;
    align-items: center;
    gap: 10px;
  }
  .brand-mark {
    width: 16px;
    height: 16px;
    background: var(--brand);
  }
  .card--brand .brand-name {
    left: 378px;
    top: 160px;
    font-size: 42px;
  }
  .facts {
    position: absolute;
    left: 300px;
    top: 174px;
    list-style: none;
    color: var(--brand);
    font-size: 20.5px;
    font-weight: 700;
    line-height: 29px;
  }
  .facts__item {
    position: relative;
    padding-left: 50px;
    margin-bottom: 27px;
  }
  .facts__item--short { padding-left: 40px; }
  .facts__item::before {
    content: "";
    position: absolute;
    left: 3px;
    top: 8px;
    width: 12px;
    height: 12px;
    background: var(--brand);
    transform: rotate(45deg);
  }
</style>
</head>
<body>

<section class="card card--info">
  <div class="card__accent" role="img" aria-label="Decorative layered green wave pattern"></div>
  <div class="brand-name"><span class="brand-mark"></span>Brivora Collective</div>
  <ul class="facts">
    <li class="facts__item">We are a healthcare recruiting,<br>wellness and education company.</li>
    <li class="facts__item">We partner with medical facilities<br>to find quality candidates.</li>
    <li class="facts__item facts__item--short">We also offer free wellness courses.</li>
  </ul>
</section>

<section class="card card--brand">
  <div class="card__accent" role="img" aria-label="Decorative layered green wave pattern"></div>
  <div class="brand-name">Brivora Collective</div>
</section>

</body>
</html>
```